Rack Card Design for an Ayurvedic Beauty Product Project

Hello, I need to have rack cards. The rack cards would be about 3 products we are showcasing at an event. I am a cosmetic company. I have a logo and basic design ideas. I have attached some product images and info. By no means am I a designer so please excuse my messy AI files. Please feel free to design this as feminine as you like. :)

Target Market(s)

Beauty industry, organic, holistic, ayurveda

Industry/Entity Type

Cosmetic

```html
<!DOCTYPE html>
<html lang="en">
<head>
<meta charset="utf-8">
<title>Velvet Lotus – Ayurvedic Breast Toner Rack Card</title>
<link rel="stylesheet" href="https://fonts.googleapis.com/css2?family=Quicksand:wght@400;500;700&display=swap">
<style>
  :root {
    --stage: #c4c4c7;
    --plum: #731f58;
    --plum-deep: #4f0c3c;
    --cream: #f3e7c2;
    --cream-soft: #fbf6e6;
    --gold: #b8894a;
    --white: #ffffff;
    --ink: #333236;
  }
  * { margin: 0; padding: 0; box-sizing: border-box; }
  html, body {
    width: 1200px;
    height: 1200px;
    overflow: hidden;
    background: var(--stage);
    font-family: "Quicksand", sans-serif;
  }
  .rack-card {
    position: absolute;
    left: 355px;
    top: 67px;
    width: 490px;
    height: 1066px;
    background: var(--white);
    overflow: hidden;
  }
  .card-backdrop {
    position: absolute;
    inset: 0;
    width: 490px;
    height: 1066px;
  }
  .brand-name {
    position: absolute;
    top: 190px;
    width: 100%;
    text-align: center;
    font-size: 16px;
    font-weight: 700;
    letter-spacing: 0.06em;
    color: var(--gold);
  }
  .product-title {
    position: absolute;
    top: 252px;
    width: 100%;
    text-align: center;
    font-weight: 400;
    font-size: 42px;
    line-height: 52px;
    color: var(--white);
  }
  .product-visual {
    position: absolute;
    left: 157px;
    top: 449px;
    width: 188px;
    height: 396px;
    border-radius: 6px 6px 14px 14px;
    background: linear-gradient(180deg, #8e2d70 0%, #7a2260 70%, #c9a366 82%, #8e6a33 100%);
  }
  .product-copy {
    position: absolute;
    top: 878px;
    width: 100%;
    text-align: center;
    font-size: 18.5px;
    line-height: 23px;
    color: var(--ink);
  }
</style>
</head>
<body>
  <article class="rack-card">
    <svg class="card-backdrop" viewBox="0 0 490 1066" aria-hidden="true">
      <defs>
        <linearGradient id="plumFill" x1="0" y1="0" x2="1" y2="1">
          <stop offset="0" stop-color="var(--plum)"/>
          <stop offset="1" stop-color="var(--plum-deep)"/>
        </linearGradient>
        <linearGradient id="creamBand" x1="0" y1="1" x2="1" y2="0">
          <stop offset="0" stop-color="var(--cream-soft)"/>
          <stop offset="1" stop-color="var(--cream)"/>
        </linearGradient>
      </defs>
      <path class="accent-band" d="M0,641 C230,635 420,560 490,413 V325 C400,500 220,590 0,597 Z" fill="url(#creamBand)"/>
      <path class="header-field" d="M0,0 H490 V325 C400,500 220,590 0,597 Z" fill="url(#plumFill)"/>
    </svg>

    <p class="brand-name">VELVET LOTUS</p>

    <h1 class="product-title">Ayurvedic<br>Firming &amp; Lifting<br>Breast Toner</h1>

    <div class="product-visual" role="img" aria-label="Product photo: plum tube of Ayurvedic Firming &amp; Lifting Breast Toner with a gold cap"></div>

    <p class="product-copy">Using all natural Ayurvedic herbs,<br>our breast toner, prepares the area<br>for maximum absorption giving<br>you the best results and<br>the most invigorating treatment.</p>
  </article>
</body>
</html>
```